Double-Gate-Fold Mailer (8-panels)

I have an 8-panel brochure/mailer that I need designed. We're looking for something very classy and professional-looking (both in the fonts and the imagery chosen), as this is for a medical educational event for doctors - and our members are very discerning.

We're open to any design idea that fits within the parameters given below, but if it helps, our primary color is PMS 295 (Hex #002e5a) and we often use PMS 452 (Hex #aaa77e) as a contrasting color.

Images using the NYC skyline or major landmarks are fine, as this will be held in NYC again this year. I have attached photos of the venues that could be used as pop-out images, faded background images or for other inspiration. (I do not have higher-resolution versions of any of the venue photos.)

More info about this event can be found here: http://qv-hsl.org/2017annualmtg/

Important Notes:

- This year's mailer needs to be 20.75" x 8.75” (flat), which will be folded down to 5.19" x 8.75" ultimately.

- I will provide final text for designer, but I have attached last year's mailer so that you can use the content from this as placeholder text. Latin text is also fine - just looking for the design right now.

- *** This year's mailer WILL NOT HAVE a registration form, so please don't include the registration form portion in your design. *** We have, however, added an extra session this year (the day before), so the extra space could be used to promote this new 4-hour event.

- In case it matters to your design, the two events will be in two different locations.

- Final deliverable must include raw files, including main project file (either .ai, .idml, or psd format) and fonts, images, etc.

Project Deadline Extended Reason: While there are a couple that are interesting and some that are close to our in-house style and tone, I haven't yet seen an outstanding entry (one that followed the directions) yet, especially with respect to subtle/minimal imagery. I would like to give it a few more days. Added Wednesday, July 19, 2017

Target Market(s)

Physicians, nurses, technologists (Please do not use stock images of physicians, nurses, etc. This is a direct-mail brochure; they will know it is for them.)

Industry/Entity Type

Education

Font styles to use
Serif
Sans Serif

Colors

Designer to choose colors to be used in the design.

Requirements
Must have
• Must have room for all content to fit. Last year's brochure is attached as an example of the amount of content there will be. I have attached the five (5) logos that will (eventually) need to be on the brochure. They can be added later either in full color or monotone.
• This year doesn't have a theme like last year. The title of the event is simply: "The 89th Annual Scientific Session & Inaugural BRQ Zelvora Competition"
Nice to have
• Nice to have a design that somehow coordinates with our logos, which, as you can see, range in color from dark blue to light blue, but this isn't necessary, as our logos can all be monotone if necessary. It would be nice if the designer could keep the horizontal-style of the art, similar to last year's, but it's not a requirement.
Should not have
• Images should be subtle, faded or pushed to the background. Please don't include stock images of people, physicians working, medical equipment, etc. (This is a highly specialized field of medicine, and generic stock images look very strange and, at best, are a misrepresentation of these doctors.) Art should not be to "cartoon-y" either or have too many distracting images.

```html
<!DOCTYPE html>
<html lang="en">
<head>
<meta charset="utf-8">
<title>Empire State Chapter – Annual Meeting Mailer</title>
<link rel="stylesheet" href="https://fonts.googleapis.com/css2?family=Questrial&family=Roboto+Condensed:wght@300;400&display=swap">
<style>
  :root{
    --navy:#0d2a5c;
    --navy-deep:#0a2350;
    --tan:#aaa77e;
    --tan-light:#c2bf9c;
    --link-blue:#22508f;
    --text:#4a4f58;
    --paper:#ffffff;
    --grey-panel:#ececec;
    --backdrop:#6fb3ae;
  }
  *{margin:0;padding:0;box-sizing:border-box}
  html,body{width:1200px;height:1200px;overflow:hidden}
  body{background:var(--backdrop);font-family:"Questrial",sans-serif;color:var(--text);position:relative}

  .spread{position:absolute;left:30px;top:359px;width:1140px;height:482px;background:var(--paper);box-shadow:0 6px 14px rgba(0,0,0,.25);overflow:hidden}
  .panel{position:absolute;top:0;height:482px;overflow:hidden}
  .panel--roster{left:0;width:284px;background:linear-gradient(90deg,#fbfbfb 0%,#f0f0f0 60%,#e2e2e2 100%)}
  .panel--venues{left:284px;width:286px;background:linear-gradient(180deg,#b5b28c 0%,var(--tan) 55%,#9f9c74 100%)}
  .panel--cover{left:570px;width:286px;background:var(--paper)}
  .panel--program{left:856px;width:284px;background:var(--grey-panel)}

  .top-band{position:absolute;left:0;top:0;width:570px;height:39px;background:var(--navy);z-index:2}
  .top-band__title{position:absolute;left:22px;top:19px;color:#fff;font-size:9.5px;letter-spacing:.1px}
  .base-strip{position:absolute;left:0;bottom:0;width:1140px;height:12px;background:var(--navy);z-index:3}

  /* roster */
  .roster-fade{position:absolute;inset:0;background:linear-gradient(100deg,rgba(255,255,255,0) 40%,rgba(190,190,190,.35) 100%)}
  .roster-block{position:absolute;font-size:5.9px;line-height:6.9px;color:#555b66}
  .roster-head{font-size:6.4px;color:var(--link-blue);text-decoration:underline;letter-spacing:.2px;margin-bottom:4px;text-transform:uppercase}
  .officer{margin-bottom:6.7px}
  .org-title{position:absolute;left:26px;font-size:8.6px;line-height:9.6px;color:var(--link-blue)}

  /* venues */
  .map{position:absolute;left:45px;width:190px;height:123px;border:4px solid var(--navy);box-shadow:2px 3px 5px rgba(0,0,0,.3)}
  .map--east{top:62px;background:linear-gradient(150deg,#2b5472 0%,#3f8fb0 45%,#7fc9dc 60%,#2b5472 100%)}
  .map--west{top:211px;background:linear-gradient(135deg,#f4f4f4 0%,#dadada 50%,#f2f2f2 100%)}
  .venue-block{position:absolute;left:0;top:357px;width:286px;height:125px;background:var(--navy);color:#e8ecf4;text-align:center;font-size:5.9px;line-height:7px;padding-top:13px}
  .venue-block p{margin-bottom:12px}

  /* cover */
  .brand{position:absolute;left:0;top:0;width:286px;height:82px;background:#fff}
  .brand__mark{position:absolute;left:34px;top:15px;width:56px;height:56px;border-radius:50%;background:var(--navy)}
  .brand__name{position:absolute;left:108px;top:28px;color:var(--navy);font-family:"Roboto Condensed",sans-serif;font-weight:300;font-size:22px;line-height:20px}
  .brand__name small{display:block;font-size:9px;line-height:12px;letter-spacing:.6px}
  .cover-art{position:absolute;left:0;top:82px}
  .tagline{position:absolute;left:21px;top:380px;font-family:"Roboto Condensed",sans-serif;font-weight:300}
  .tagline__lead{font-size:38px;line-height:36px;color:#1d2128}
  .tagline__line{font-size:14.6px;line-height:19px;color:#fff;letter-spacing:.3px}
  .tagline__line--navy{color:var(--navy);font-size:16px;letter-spacing:.5px}

  /* program */
  .program-band{position:absolute;left:0;top:0;width:284px;height:17px;background:var(--navy)}
  .program-band::after{content:"";position:absolute;left:0;top:17px;width:284px;height:5px;background:#d6d6d6}
  .program-body{position:absolute;left:15px;top:29px;width:250px;font-size:5.7px;line-height:6.9px;color:#4b4f56}
  .program-body h2{font-weight:400;font-size:8.6px;line-height:10px;color:var(--link-blue);margin:2px 0 1px}
  .program-body p{text-align:justify;margin-bottom:2px}
  .objectives{list-style:none;margin-top:3px}
  .objectives li{position:relative;padding-left:15px;margin-bottom:4.1px;text-align:justify}
  .objectives li::before{content:"";position:absolute;left:2px;top:1.5px;width:4px;height:4px;background:var(--navy)}
</style>
</head>
<body>
<main class="spread">

  <div class="top-band"><span class="top-band__title">The Hudson Cardiological Society, Inc.</span></div>

  <!-- Panel: leadership roster -->
  <section class="panel panel--roster">
    <div class="roster-fade" role="img" aria-label="Faded photograph of a harbour statue and suspension bridge"></div>

    <div class="roster-block" style="left:26px;top:56px">
      <div class="roster-head">Officers</div>
      <div class="officer">Tobias R. Merrin, MD, FACC<br>President</div>
      <div class="officer">Warren Lindqvist, MD, FACC<br>Immediate Past President</div>
      <div class="officer">Thomas Delvaux, MD, FACC<br>Secretary-Treasurer</div>
      <div class="officer">Marian Pellham, MA, MSA<br>Executive Director</div>
    </div>
    <div class="roster-block" style="left:151px;top:56px">
      <div class="roster-head">Executive Board</div>
      Jonah Brevard, MD, PhD<br>Julian S. Boyce, MD<br>Lewis Chandra, MD, MPH<br>Peter F. Calder, MD<br>Paul Kettering, MD<br>Selma Korven, MD<br>Joel Lachance, MD<br>Warren E. Lindqvist, MD<br>Tobias R. Merrin, MD<br>James T. Morello, MD<br>Harry C. Ostrander, Jr.,MD<br>Harold Sterne, MD<br>Andrew Van Helt, MD<br>Daniel J. Whitcombe, MD<br>Malik Zaheen, MD
    </div>

    <div class="org-title" style="top:179px">Metro Cardiac Center</div>
    <div class="roster-block" style="left:26px;top:194px">
      <div class="roster-head">Officers</div>
      <div class="officer">Russell J. Garner<br>President</div>
      <div class="officer">Martin J. Wexler, MD<br>Executive Vice President</div>
      <div class="officer">Daniel M. Carrow, MD<br>Secretary</div>
      <div class="officer">Albert S. Granger<br>Treasurer</div>
    </div>
    <div class="roster-block" style="left:151px;top:194px">
      <div class="roster-head">Board of Governors</div>
      Miles Bancroft, DDS<br>Edwin Brandt<br>Daniel M. Carrow, MD<br>Hon. Bernard Gilroy<br>Dennis Gartner, Esq.<br>Russell J. Garner<br>Albert S. Granger<br>Jerome Galloway<br>Evan Marlowe, Esq.<br>Jeffrey Prentiss<br>Michael Rowland, DDS<br>Lena Tarrant, MD<br>Martin J. Wexler, MD<br>Robert Wexler
    </div>

    <div class="org-title" style="top:316px">Empire State Chapter, Atlantic College<br>of Cardiology</div>
    <div class="roster-block" style="left:26px;top:340px">
      <div class="roster-head">Officers</div>
      <div class="officer">Warren Lindqvist, MD, FACC<br>President</div>
      <div class="officer">Tobias R. Merrin, MD, FACC<br>Immediate Past President</div>
      <div class="officer">Thomas Delvaux, MD, FACC<br>Secretary-Treasurer</div>
      <div class="officer">Marian Pellham, MA, MSA<br>Executive Director</div>
    </div>
    <div class="roster-block" style="left:151px;top:340px">
      <div class="roster-head">Councilors</div>
      Ronald Cheswick, MD, New Rochelle<br>Jay J. Dunmore, MD, Manhasset<br>Dmitri N. Fallon, MD, Manhattan<br>Stanley F. Ferraro, MD, Buffalo<br>Seth Ivers, MD, Valhalla<br>Nora M. Kessler, MD, Manhattan<br>Lloyd D. Lomax, MD, Stony Brook<br>Charles J. Lindell, MD, Rochester<br>Amir N. Malouf, MD, East Meadow<br>Arun R. Pandit, MD, Utica<br>Robert S. Pryor, MD, Albany<br>Brian J. Rourke, MD, Buffalo<br>Michael A. Selden, MD, Utica<br>Benjamin M. Stratton, MD, Rhinebeck<br>Manish S. Sethi, MD, Albany<br>John Chad Tolliver, MD, Rochester<br>Theodore J. Talbot, MD, Manhattan
    </div>
  </section>

  <!-- Panel: venues -->
  <section class="panel panel--venues">
    <div class="map map--east" role="img" aria-label="Map of the first meeting venue neighbourhood in Manhattan"></div>
    <div class="map map--west" role="img" aria-label="Street map of the second meeting venue location"></div>
    <div class="venue-block">
      <p>The Hudson Cardiological Society, Inc.</p>
      <p>410 Harbor Avenue, Suite 1207<br>New York, NY 10021</p>
      <p>89th Annual Scientific Session<br>The Hudson Cardiological Society, Inc.</p>
      <p>26th Annual Meeting<br>Empire State Chapter,<br>Atlantic College of Cardiology</p>
    </div>
  </section>

  <!-- Panel: cover -->
  <section class="panel panel--cover">
    <div class="brand">
      <span class="brand__mark" aria-hidden="true"></span>
      <div class="brand__name">Empire State<small>CHAPTER</small></div>
    </div>
    <svg class="cover-art" width="286" height="400" viewBox="0 0 286 400">
      <defs>
        <linearGradient id="skyline" x1="0" y1="0" x2="0" y2="1">
          <stop offset="0" stop-color="#c8d3e3"/>
          <stop offset=".3" stop-color="#f1d3c8"/>
          <stop offset=".55" stop-color="#b9a79a"/>
          <stop offset=".8" stop-color="#6a5a4f"/>
          <stop offset="1" stop-color="#3e3632"/>
        </linearGradient>
      </defs>
      <rect x="0" y="0" width="286" height="8" fill="#0d2a5c"/>
      <rect x="0" y="8" width="286" height="300" fill="url(#skyline)" role="img" aria-label="Photograph of the Manhattan skyline at sunrise with a landmark tower"/>
      <polygon points="0,270 286,214 286,224 0,280" fill="#0d2a5c"/>
      <polygon points="0,279 286,223 286,400 0,400" fill="#aaa77e"/>
    </svg>
    <div class="tagline">
      <div class="tagline__lead">New York is home</div>
      <div class="tagline__line">TO THE OLDEST CARDIOLOGOCAL</div>
      <div class="tagline__line tagline__line--navy">ORGANIZATION IN THE NATION</div>
    </div>
  </section>

  <!-- Panel: program -->
  <section class="panel panel--program">
    <div class="program-band"></div>
    <div class="program-body">
      <h2>Program Description</h2>
      <p>As cardiovascular medicine rapidly evolves, cardiovascular healthcare providers are challenged to determine and recommend the best therapies for their patients. This scientific session provides attendees with the opportunity to examine current topics with the goal of helping them provide the best care for their aging patients. The program will include presentations from nationally respected cardiovascular specialists from around the country. Among the lectures, the topics will center around acute myocardial infarction, non-invasive imaging for diagnosis of cardiac amyloidosis, telemonitoring, readmission reduction, atrial fibrillation, aortic stenosis, and post-acute cardiovascular care in older adults. Exhibitors will present materials relevant to some of the advances in therapy being discussed. Regular breaks will allow for networking and the ability for fellows in training (FITs) and other cardiovascular clinicians to meet with and to discuss issues relevant to their future and the current practice of cardiology. In addition, the winners of the Young Investigators research competition will display posters of their scientific work, and two clinical case presentations will be briefly presented by the winning fellows of the case competition and discussed by their cardiology mentors.</p>
      <h2>Target Audience</h2>
      <p>The target audience includes cardiologists, cardiothoracic surgeons, internists, family medicine practitioners, gerontologists, oncologists, cardiac nurse practitioners, physician assistants, cardiology fellows-in-training and all members of the cardiac care team.</p>
      <h2>Program Objectives</h2>
      <p>At the completion of this program, physicians and other healthcare professionals in attendance will be able to:</p>
      <ul class="objectives">
        <li>Explain the rationale for, and identify components of, a comprehensive approach to readmission reduction</li>
        <li>Describe the importance of high-quality, disease-specific care, multiple transitional care interventions, involvement of multidisciplinary teams, and early and frequent outpatient followup</li>
        <li>Navigate the current landscapes of Post-Acute Care and describe its relevance in the care of our geriatric cardiology patients<br>Identify gaps in care and specific interventions providers can utilize to improve outcomes</li>
        <li>Identify various types of procedures necessary for treating atrial fibrillation in older adults</li>
        <li>Explain the rationale for why the management of atrial fibrillation is directed at preventing thromboembolism and controlling heart rate and rhythm</li>
        <li>Identify the effects of aging on CV care and unique aspects of care for older adults</li>
        <li>Delineate the various phenotypes of aortic stenosis in older adults and enumerate mechanisms underlying paradoxically low-flow aortic stenosis</li>
        <li>Identify TTR Cardiac amyloid without a biopsy</li>
        <li>Explain the extent to which current guidelines for cardiovascular disorders are evidence-based with respect to older adults</li>
        <li>Identify strategies for improving care and outcomes for older adults with cardiovascular diseases</li>
        <li>Describe the role of non-invasive imaging for diagnosis of cardiac amyloidosis</li>
        <li>Recite promising treatments for TTR cardiac amyloidosis</li>
        <li>Describe ways in which telemonitoring can improve heart failure outcomes</li>
        <li>Describe patients' perspectives about the pros and cons of telemonitoring</li>
        <li>Identify management strategies in diagnosing acute MI in elderly patients</li>
      </ul>
    </div>
  </section>

  <div class="base-strip"></div>
</main>
</body>
</html>
```